Web Design for Financial Consulting Company

We need a website design for a financial consulting company "Korvane Consulting". We build financial models, scenario analysis, handle the budgeting process and provide temporary staffing. I have over 10 years of experience. My Excel expertise and analytical savvy has saved clients over $17 million in profit.

Target Market(s)

Small to medium businesses

Industry/Entity Type

Financial Consulting

Number of Pages Required

4 page

Requirements
Must have
• Professional looking
Nice to have
• A little futuristic looking

```html
<!DOCTYPE html>
<html lang="en">
<head>
<meta charset="utf-8">
<title>Korvane Consulting</title>
<link href="https://fonts.googleapis.com/css2?family=Poppins:wght@300;400;500;600;700&display=swap" rel="stylesheet">
<style>
:root{
  --blue:#0ba3ee;
  --navy:#0f3c68;
  --ink:#1d2b3a;
  --muted:#8a94a0;
  --white:#ffffff;
  --field:#ffffff;
  --light:#eef1f4;
}
*{margin:0;padding:0;box-sizing:border-box}
html,body{width:1200px;height:3504px;overflow:hidden}
body{font-family:'Poppins',sans-serif;color:var(--ink);background:var(--white);position:relative}
.abs{position:absolute}
.topbar{left:0;top:0;width:1200px;height:38px;background:var(--blue);color:var(--white);font-size:14px}
.topbar span{position:absolute;top:10px;display:flex;align-items:center;gap:8px}
.header{left:0;top:38px;width:1200px;height:101px;background:var(--white)}
.brand{display:flex;align-items:center;gap:10px}
.brand-mark{width:40px;height:40px;border:4px solid var(--blue)}
.brand-name{font-weight:600;color:var(--navy);font-size:30px;line-height:1;letter-spacing:1px}
.brand-sub{font-size:12px;letter-spacing:12px;color:var(--blue);font-weight:400;margin-top:4px}
.nav{top:76px;font-size:15px;color:var(--navy);font-weight:400}
.nav.active{color:var(--blue)}
.nav.active::before{content:"";display:inline-block;width:7px;height:7px;background:var(--blue);margin-right:7px;vertical-align:2px}
.hero{left:0;top:139px;width:1200px;height:694px;background:linear-gradient(100deg,#e9eef2 0%,#dfe4e8 45%,#9aa4ac 70%,#3c4856 100%)}
.hero h1{position:absolute;left:137px;top:146px;font-weight:300;font-size:49px;line-height:55px;color:var(--navy)}
.hero h1 strong{font-weight:600;color:var(--blue);display:block}
.dot{width:15px;height:15px;border-radius:50%;top:603px}
.section-title{display:flex;align-items:center;gap:10px}
.title-mark{width:44px;height:44px;border:4px solid var(--blue)}
.section-title h2{font-size:31px;font-weight:600;color:var(--navy);line-height:1}
.section-title small{display:block;font-size:14px;letter-spacing:6px;color:var(--blue);margin-top:2px}
.about-img{left:178px;top:948px;width:360px;height:267px;border-radius:10px;background:linear-gradient(135deg,#c9c1b4,#8d8a86 50%,#e3ddd3)}
.about-text{left:585px;top:1068px;width:470px;font-size:15.5px;line-height:31px;color:#222}
.card{overflow:hidden}
.card .photo{position:absolute;inset:0}
.card .label{position:absolute;left:0;right:0;bottom:0;background:rgba(30,30,30,.55);color:var(--white);font-weight:600;font-size:20px;text-align:center;line-height:25px;padding:12px 10px}
.card.featured .photo{background:linear-gradient(160deg,#2f6fa0,#174b78)}
.card.featured .inner{position:absolute;left:0;right:0;top:100px;text-align:center;color:var(--white);padding:0 40px}
.card.featured h3{font-size:20px;font-weight:600;line-height:25px}
.card.featured hr{width:44px;border:0;border-top:1px solid var(--white);margin:12px auto}
.card.featured p{font-size:15.5px;line-height:26px}
.contact{left:0;top:2310px;width:1200px;height:800px;background:linear-gradient(120deg,#e8ebef,#f3f4f6 50%,#e3e6ea)}
.field{background:var(--field);border-radius:8px;color:var(--muted);font-size:17px;display:flex;align-items:center;gap:16px;padding-left:32px}
.field.tall{align-items:flex-start;padding-top:24px}
.btn{left:494px;top:2909px;width:219px;height:60px;background:var(--blue);color:var(--white);border-radius:8px;font-size:16px;font-weight:500;display:flex;align-items:center;justify-content:center}
.footer{left:0;width:1200px;background:var(--navy)}
.foot-h{font-size:20px;color:var(--blue);font-weight:500}
.foot-h::after{content:"";display:block;width:34px;height:2px;background:var(--blue);margin-top:4px}
.foot-link{font-size:15px;color:var(--white)}
.foot-link::before{content:"›";margin-right:12px}
.foot-item{display:flex;align-items:center;gap:16px;color:var(--white);font-size:15px;line-height:18px}
.icon-box{width:32px;height:32px;border:1px solid var(--white);border-radius:5px;display:flex;align-items:center;justify-content:center;flex:none}
.copy{left:0;top:3446px;width:1200px;height:58px;background:var(--blue);color:var(--navy);font-size:14px;display:flex;align-items:center;justify-content:center}
</style>
</head>
<body>

<div class="abs topbar">
  <span style="left:748px"><svg width="16" height="16" viewBox="0 0 16 16" fill="none" stroke="#fff" stroke-width="1.5"><path d="M4 2l2 3-1.5 1.5a8 8 0 005 5L11 10l3 2-1.5 2.5C7 14 2 9 1.5 3.5z"/></svg>012-478-2390</span>
  <span style="left:912px;font-size:13px"><svg width="20" height="14" viewBox="0 0 20 14" fill="none" stroke="#fff" stroke-width="1.5"><rect x="1" y="1" width="18" height="12"/><path d="M1 1l9 7 9-7"/></svg>HELLO@KORVANE-MAIL.COM</span>
</div>

<div class="abs header">
  <div class="abs brand" style="left:86px;top:26px">
    <div class="brand-mark"></div>
    <div><div class="brand-name">KORVANE</div><div class="brand-sub">CONSULTING</div></div>
  </div>
</div>
<div class="abs nav active" style="left:706px">HOME</div>
<div class="abs nav" style="left:801px">ABOUT US</div>
<div class="abs nav" style="left:913px">SERVICES</div>
<div class="abs nav" style="left:1019px">CONTACT US</div>

<section class="abs hero" role="img" aria-label="Photo of a finance professional in glasses working on a laptop in a bright office">
  <h1>Helping your<br>finance team and<strong>Increasing Profit</strong></h1>
  <svg class="abs" style="left:0;top:624px" width="1200" height="70" viewBox="0 0 1200 70"><polygon points="0,70 1200,70 1200,0 0,70" fill="#fff"/><polygon points="150,66 1200,12 1200,40 0,70" fill="var(--blue)"/><polygon points="0,70 1200,40 1200,70" fill="#fff"/></svg>
  <div class="abs dot" style="left:592px;background:#fff"></div>
  <div class="abs dot" style="left:612px;background:var(--blue)"></div>
  <div class="abs dot" style="left:631px;background:var(--blue)"></div>
</section>

<div class="abs about-img" role="img" aria-label="Photo of a small team gathered around a laptop"></div>
<div class="abs section-title" style="left:584px;top:990px">
  <div class="title-mark"></div>
  <div><h2>ABOUT US</h2><small>WHO WE ARE</small></div>
</div>
<p class="abs about-text">I am an experienced Finance professional who develops strategic financial plans, provides insightful analysis, and supports decision-making. With over 10 years of experience, I have successfully increased profitability for clients by $17M.</p>

<div class="abs section-title" style="left:490px;top:1385px">
  <div class="title-mark"></div>
  <div><h2>SERVICES</h2><small>WHAT WE DO</small></div>
</div>

<div class="abs card" style="left:87px;top:1516px;width:314px;height:378px">
  <div class="photo" role="img" aria-label="Photo of a woman reviewing notes at a desk" style="background:linear-gradient(160deg,#e6e4e0,#b9a898 60%,#6d655d)"></div>
  <div class="label">FINANCIAL<br>MODELS – PROJECTS</div>
</div>
<div class="abs card featured" style="left:446px;top:1516px;width:315px;height:378px">
  <div class="photo" role="img" aria-label="Photo of a hand working on a tablet, tinted blue"></div>
  <div class="inner"><h3>BUDGETING<br>PROCESS</h3><hr><p>Building budgets from scratch, revamping current process to be more robust and scalable.</p></div>
</div>
<div class="abs card" style="left:801px;top:1516px;width:315px;height:378px">
  <div class="photo" role="img" aria-label="Photo of three colleagues working at a meeting table" style="background:linear-gradient(160deg,#f0f0ef,#c9c4c0 55%,#7c716d)"></div>
  <div class="label" style="background:transparent">TEMPORARY<br>STAFFING</div>
</div>
<div class="abs card" style="left:87px;top:1935px;width:502px;height:291px">
  <div class="photo" role="img" aria-label="Photo of a laptop and camera on a wooden desk" style="background:linear-gradient(150deg,#bfbcb5,#7a6a5c 55%,#3d3430)"></div>
  <div class="label" style="padding:38px 10px 22px">DATA CLEANSING</div>
</div>
<div class="abs card" style="left:612px;top:1935px;width:502px;height:291px">
  <div class="photo" role="img" aria-label="Photo of a man working at a computer in an office" style="background:linear-gradient(150deg,#e3e1dc,#9b9690 55%,#46423f)"></div>
  <div class="label" style="padding:38px 10px 22px">PROCESS IMPROVEMENT</div>
</div>

<div class="abs contact" role="img" aria-label="Photo of a desk top with keyboard, phone, paper clips, pencils and a plant"></div>
<div class="abs section-title" style="left:490px;top:2410px">
  <div class="title-mark"></div>
  <div><h2>CONTACT US</h2><small style="letter-spacing:2px">HOW CAN WE HELP YOU</small></div>
</div>
<div class="abs field" style="left:173px;top:2552px;width:422px;height:66px"><svg width="14" height="16" viewBox="0 0 14 16" fill="#9aa3ad"><circle cx="7" cy="4.5" r="4"/><path d="M0 16c0-5 3-7 7-7s7 2 7 7z"/></svg>First Name</div>
<div class="abs field" style="left:604px;top:2552px;width:423px;height:66px"><svg width="18" height="13" viewBox="0 0 18 13" fill="#9aa3ad"><rect width="18" height="13"/><path d="M0 0l9 7 9-7" stroke="#fff" fill="none"/></svg>E-Mail</div>
<div class="abs field" style="left:173px;top:2649px;width:422px;height:66px"><svg width="12" height="16" viewBox="0 0 12 16" fill="none" stroke="#9aa3ad" stroke-width="1.5"><rect x="1" y="1" width="10" height="14" rx="1.5"/></svg>Phone Number</div>
<div class="abs field" style="left:605px;top:2649px;width:423px;height:66px"><svg width="12" height="16" viewBox="0 0 12 16" fill="#9aa3ad"><path d="M6 0a6 6 0 016 6c0 4-6 10-6 10S0 10 0 6a6 6 0 016-6z"/><circle cx="6" cy="6" r="2" fill="#fff"/></svg>Address</div>
<div class="abs field tall" style="left:173px;top:2746px;width:856px;height:130px"><svg width="16" height="16" viewBox="0 0 16 16" fill="#9aa3ad"><circle cx="8" cy="8" r="8"/></svg>Message</div>
<div class="abs btn">SUBMIT NOW</div>

<svg class="abs" style="left:0;top:3020px" width="1200" height="90" viewBox="0 0 1200 90"><polygon points="0,10 1200,68 1200,90 0,90" fill="var(--navy)"/><polygon points="380,28 1200,54 1200,84" fill="var(--blue)"/></svg>
<div class="abs footer" style="top:3105px;height:341px"></div>

<div class="abs" style="left:190px;top:3184px;width:112px;height:112px;border:6px solid var(--blue)"></div>
<div class="abs" style="left:122px;top:3318px;width:250px;text-align:center">
  <div style="font-size:38px;font-weight:600;color:var(--white);letter-spacing:2px;line-height:1">KORVANE</div>
  <div style="font-size:13px;letter-spacing:16px;color:var(--blue);margin-top:6px">CONSULTING</div>
</div>

<div class="abs foot-h" style="left:427px;top:3170px">Quick Links</div>
<div class="abs foot-link" style="left:433px;top:3252px">Home</div>
<div class="abs foot-link" style="left:433px;top:3283px">About Us</div>
<div class="abs foot-link" style="left:433px;top:3314px">Services</div>
<div class="abs foot-link" style="left:433px;top:3344px">Contact Us</div>

<div class="abs foot-h" style="left:619px;top:3170px">Contact Us</div>
<div class="abs foot-item" style="left:620px;top:3256px"><div class="icon-box"><svg width="14" height="14" viewBox="0 0 16 16" fill="none" stroke="#fff" stroke-width="1.5"><path d="M4 2l2 3-1.5 1.5a8 8 0 005 5L11 10l3 2-1.5 2.5C7 14 2 9 1.5 3.5z"/></svg></div><div>CALL US<br>7204 918 3365</div></div>
<div class="abs foot-item" style="left:620px;top:3312px"><div class="icon-box"><svg width="14" height="10" viewBox="0 0 18 13" fill="#fff"><rect width="18" height="13"/></svg></div><div>EMAIL US<br>hello@korvane-mail.com</div></div>
<div class="abs foot-item" style="left:620px;top:3367px"><div class="icon-box"><svg width="10" height="14" viewBox="0 0 12 16" fill="#fff"><path d="M6 0a6 6 0 016 6c0 4-6 10-6 10S0 10 0 6a6 6 0 016-6z"/></svg></div><div>Address line Dummy Here<br>Address line Here</div></div>

<div class="abs foot-h" style="left:913px;top:3170px">Follow Us</div>
<div class="abs foot-item" style="left:916px;top:3255px"><div class="icon-box"></div>CIRCLEHUB</div>
<div class="abs foot-item" style="left:916px;top:3308px"><div class="icon-box"></div>CHIRPLINE</div>
<div class="abs foot-item" style="left:916px;top:3360px"><div class="icon-box"></div>SNAPFRAME</div>

<div class="abs copy">Copyright © 2023 All Rights Reserved By Korvane Consulting</div>

</body>
</html>
```